Wizards Among Humbug Trades*

I am looking for a book cover which will really pop. Working title: Wizards Among Humbug Trades (or W.A.H.T. for short) The concept behind the book is: education is too expensive, screwed up, and basically failing us, and even an MBA is not worth it's name anymore! How a BS is Brilliantly Stupid, a BA is great to be a Broke Artist, an MA is Mostly Antiquated and a MS Mastered Something? ...you get the point, basically I'll be ripping into a whole bunch of degree types, then walking you through what you should actually learn from an MBA. It is going to be written with a fair bit of humor, while still being fact driven. Target audience is working professionals who are considering an MBA, or have one and want a $15 refresher of all they spent $90k+ on. No color scheme is requested, Since i do like to allow creativity to flow!

Book size 5" by 8" and ebook. Author is: L.K. Brannigan size format attached.

Went on vacation/holiday

Colors

Requirements
Must have
• W.A.H.T. (but can be an emphasises in the Wizards Among Humbug Trades title.
Nice to have
• If you look at "A quiet orchard year: notes on tending pears while raising twin goats" on quorvel, you can see a blue/silver/white color scheme I liked in the past - but dont take that as a must by any means, the second choice was a completely different (red and white) scheme

```html
<!DOCTYPE html>
<html lang="en">
<head>
<meta charset="utf-8">
<title>Wizards Among Humbug Trades — L.K. Brannigan</title>
<link rel="stylesheet" href="https://fonts.googleapis.com/css2?family=Bebas+Neue&family=EB+Garamond:ital@0;1&display=swap">
<style>
  :root {
    --page-bg: #eceef2;
    --cover-bg: #ffffff;
    --ink-navy: #272c3f;
    --ink-blue: #3563b1;
    --accent-orange: #ef5a24;
    --band-text: #ffffff;
  }
  html, body {
    margin: 0;
    padding: 0;
    overflow: hidden;
  }
  body {
    width: 1200px;
    height: 1103px;
    background: var(--page-bg);
    position: relative;
  }
  .book-cover {
    position: absolute;
    left: 245px;
    top: 20px;
    width: 709px;
    height: 1063px;
    display: block;
    box-shadow: 0 6px 24px rgba(20, 24, 40, 0.18);
  }
  .cover-bg { fill: var(--cover-bg); }
  .title-condensed {
    font-family: "Bebas Neue", "Oswald", sans-serif;
    text-anchor: middle;
  }
  .title-navy { fill: var(--ink-navy); }
  .title-blue { fill: var(--ink-blue); }
  .title-connector {
    font-family: "EB Garamond", Georgia, serif;
    font-style: italic;
    fill: var(--ink-navy);
    text-anchor: middle;
  }
  .acronym {
    font-family: "EB Garamond", Georgia, serif;
    fill: var(--ink-blue);
  }
  .pointer-arrow {
    fill: none;
    stroke: var(--accent-orange);
    stroke-width: 9;
    stroke-linecap: round;
  }
  .pointer-head { fill: var(--accent-orange); }
  .author-band { fill: var(--ink-navy); }
  .author-name {
    font-family: "Bebas Neue", "Oswald", sans-serif;
    fill: var(--band-text);
    text-anchor: middle;
  }
</style>
</head>
<body>
  <svg class="book-cover" viewBox="0 0 859 1288" role="img" aria-label="Book cover: Wizards Among Humbug Trades by L.K. Brannigan">
    <rect class="cover-bg" x="0" y="0" width="859" height="1288"/>

    <g class="title-block">
      <text class="title-condensed title-navy" x="429" y="357" font-size="240" textLength="677" lengthAdjust="spacingAndGlyphs">WIZARDS</text>
      <text class="title-connector" x="432" y="455" font-size="92">among</text>
      <text class="title-condensed title-blue" x="430" y="610" font-size="161" textLength="560" lengthAdjust="spacing">HUMBUG</text>
      <text class="title-condensed title-navy" x="432" y="854" font-size="286" textLength="540" lengthAdjust="spacingAndGlyphs">TRADES</text>
    </g>

    <g class="acronym-pointer">
      <path class="pointer-arrow" d="M140 618 C 100 720, 30 860, 60 905 C 95 955, 170 948, 228 946"/>
      <path class="pointer-head" d="M196 922 L 252 947 L 196 964 L 214 946 Z"/>
    </g>

    <text class="acronym" x="272" y="1007" font-size="128" textLength="534" lengthAdjust="spacing">W.A.H.T.</text>

    <g class="author">
      <rect class="author-band" x="0" y="1162" width="859" height="126"/>
      <text class="author-name" x="430" y="1257" font-size="86" textLength="572" lengthAdjust="spacingAndGlyphs">L.K. BRANNIGAN</text>
    </g>
  </svg>
</body>
</html>
```